Online trading school - Website design

We are building an online trading school (trading of shares, commodities, indices, currencies). The purpose is to teach online traders how to trade successfully. We need to design the homepage of the website and logo (bramwelloq.com will be the domain). The homepage will contain the following elements

- logo
- Sign in and Register links/buttons
- upper menu
- short introduction
- a couple of bullet points 'Why to join our school?'
- sign up form
- text
- bottom menu

Attached is a draft for the designer. The draft is just for an inspiration, the actual structure of the website can be different if the designer thinks so.

The designer is free to choose colors.

School

3 page

```html
<!DOCTYPE html>
<html lang="en">
<head>
<meta charset="utf-8">
<title>Online Trading School</title>
<link href="https://fonts.googleapis.com/css2?family=Raleway:ital,wght@0,400;0,500;0,600;0,700;1,400;1,500&display=swap" rel="stylesheet">
<style>
:root{
  --page:#ececec;
  --white:#ffffff;
  --red:#cc0000;
  --dark:#232323;
  --nav-line:#3c3c3c;
  --muted:#555;
  --text:#333;
  --band:#aab0b5;
  --band-dark:#979ea3;
  --blue:#3a8fc1;
  --footer:#222327;
  --peach:#f8cfa8;
}
*{box-sizing:border-box;margin:0;padding:0}
html,body{width:1200px;height:1136px;overflow:hidden}
body{background:var(--page);font-family:"Raleway",sans-serif;color:var(--text);position:relative}
.abs{position:absolute}
.topbar{left:0;top:0;width:1200px;height:46px;border-bottom:1px solid #dcdcdc}
.account{right:126px;top:16px;display:flex;gap:24px;font-size:13px}
.account span{display:flex;align-items:center;gap:4px}
.account .register{color:#777}
.account .signin{color:var(--red)}
.logo{left:124px;top:62px;font-size:18px;font-weight:600;color:var(--red)}
.social{left:970px;top:63px;display:flex;gap:6px}
.social span{width:31px;height:31px;border-radius:50%;background:#8a9096;display:block}
.frame{left:125px;top:117px;width:949px;height:334px;background:var(--white);border-radius:4px;border:1px solid #dadada}
.nav{left:129px;top:121px;width:941px;height:44px;background:var(--dark);display:flex;font-size:13px;color:#ddd;border-radius:3px 3px 0 0}
.nav a{display:flex;align-items:center;justify-content:center;height:44px;color:inherit;text-decoration:none;border-right:1px solid var(--nav-line)}
.nav a.active{color:var(--red)}
.search{left:798px;top:126px;width:267px;height:32px;background:#363636;border-radius:2px}
.search em{position:absolute;left:37px;top:8px;font-size:12px;color:#888}
.search .go{position:absolute;right:0;top:0;width:45px;height:32px;background:var(--blue)}
.hero{left:129px;top:165px;width:941px;height:282px;background:linear-gradient(100deg,#f1eeec 0%,#f2e2d2 35%,#c9b7a4 55%,#8e8a86 75%,#6f727a 100%)}
.hero h1{position:absolute;left:40px;top:114px;font-size:25px;font-weight:400;color:var(--red)}
.hero p{position:absolute;left:40px;top:150px;font-size:13.5px;font-weight:600;color:#222;line-height:18px}
.btn{background:var(--red);color:#fff;font-size:14px;display:flex;align-items:center;justify-content:center}
.hero .btn{position:absolute;left:40px;top:196px;width:114px;height:36px}
.card{background:var(--white);border:1px solid #dadada;border-radius:3px}
.band{height:39px;background:var(--band);color:#fff;font-size:13.5px;font-weight:600;display:flex;align-items:center}
.band .arrow{width:42px;height:39px;background:var(--band-dark);display:flex;align-items:center;justify-content:center}
.band h2{font-size:13.5px;font-weight:600;padding-left:16px}
.why{left:126px;top:462px;width:550px;height:304px}
.why .band{margin:4px 4px 0 4px}
.reasons{position:absolute;left:47px;top:66px;list-style:none;font-size:14px;color:#333}
.reasons li{display:flex;align-items:center;gap:9px;height:36px}
.student{position:absolute;left:296px;top:58px;width:253px;height:245px;background:radial-gradient(ellipse at 60% 55%,#3a4f7a 0%,#7c8aa6 40%,rgba(255,255,255,0) 72%)}
.join{left:688px;top:462px;width:387px;height:304px}
.join .band{margin:4px 5px 0 4px}
.field{position:absolute;left:58px;width:217px;height:36px;border:1px solid #cfcfcf;font-size:13px;color:#666;padding:10px 13px}
.agree{position:absolute;left:60px;top:214px;display:flex;align-items:center;gap:6px;font-size:14px;font-style:italic;color:#444}
.radio{width:14px;height:14px;border-radius:50%;border:1px solid #ccc;display:flex;align-items:center;justify-content:center}
.radio i{width:6px;height:6px;border-radius:50%;background:var(--red)}
.join .btn{position:absolute;left:60px;top:245px;width:100px;height:37px}
.offers{left:125px;top:774px;width:951px;height:225px;background:var(--peach);overflow:hidden}
.offers .band{position:absolute;left:5px;top:4px;width:938px;z-index:2}
.offers .band h2{flex:1;text-align:center;padding:0 42px 0 0}
.offers-visual{position:absolute;left:0;top:44px;width:560px;height:181px;background:linear-gradient(90deg,#4c7f77 0%,#8ea9a1 30%,#c7b7a3 60%,var(--peach) 100%)}
.offers p{position:absolute;left:440px;top:78px;width:480px;font-size:13px;line-height:21px;color:#333}
.offers p b{color:var(--red);font-weight:600;margin-left:6px}
.footer{left:0;top:1024px;width:1200px;height:112px;background:var(--footer);color:#eee;text-align:center}
.footer .links{position:absolute;top:34px;width:100%;font-size:14px;font-style:italic}
.footer .links span{margin:0 16px}
.footer .copy{position:absolute;top:68px;width:100%;font-size:14px}
</style>
</head>
<body>
<header class="abs topbar">
  <div class="abs account">
    <span class="register"><svg width="14" height="16" viewBox="0 0 14 16"><rect x="2" y="7" width="10" height="8" fill="none" stroke="#888" stroke-width="1.4"/><path d="M4 7V4.5a3 3 0 0 1 6 0V7" fill="none" stroke="#888" stroke-width="1.4"/></svg>Register</span>
    <span class="signin"><svg width="16" height="16" viewBox="0 0 16 16"><circle cx="8" cy="8" r="6.5" fill="none" stroke="#cc0000" stroke-width="1.6"/><path d="M3 8h7M7 5l3 3-3 3" fill="none" stroke="#cc0000" stroke-width="1.6"/></svg>Sign in now</span>
  </div>
</header>
<div class="abs logo">MAIN LOGO WILL BE HERE</div>
<div class="abs social" aria-label="Social links"><span></span><span></span><span></span></div>

<div class="abs frame"></div>
<nav class="abs nav">
  <a class="active" style="width:178px">ABOUT OUR SCHOOL</a>
  <a style="width:137px">RISK WARNING</a>
  <a style="width:74px">FAQ</a>
  <a style="width:169px">TRADING GLOSSARY</a>
  <a style="width:103px">CONTACT</a>
</nav>
<div class="abs search"><em>Search Web and Directory</em><span class="go"><svg width="45" height="32" viewBox="0 0 45 32"><circle cx="21" cy="15" r="6" fill="none" stroke="#fff" stroke-width="1.8"/><path d="M25.5 19.5 30 24" stroke="#fff" stroke-width="1.8"/></svg></span></div>

<section class="abs hero" role="img" aria-label="Photo of students working on laptops at a desk">
  <h1>we are an online trading school.</h1>
  <p>we teach trading of shares, commodities,<br>indices, currencies</p>
  <a class="btn">Learn More ›</a>
</section>

<section class="abs card why">
  <div class="band"><span class="arrow"><svg width="12" height="18" viewBox="0 0 12 18"><path d="M2 1l8 8-8 8" fill="none" stroke="#fff" stroke-width="1.8"/></svg></span><h2>WHY TO JOIN US?</h2></div>
  <ul class="reasons">
    <li><svg width="17" height="14" viewBox="0 0 17 14"><path d="M1 7l5 5L16 1" fill="none" stroke="#777" stroke-width="2"/></svg>Best trading tips ever</li>
    <li><svg width="17" height="14" viewBox="0 0 17 14"><path d="M1 7l5 5L16 1" fill="none" stroke="#777" stroke-width="2"/></svg>Secret tips from expets</li>
    <li><svg width="17" height="14" viewBox="0 0 17 14"><path d="M1 7l5 5L16 1" fill="none" stroke="#777" stroke-width="2"/></svg>We teach you how to trade online</li>
    <li><svg width="17" height="14" viewBox="0 0 17 14"><path d="M1 7l5 5L16 1" fill="none" stroke="#777" stroke-width="2"/></svg>Learn how to trade commodities</li>
    <li><svg width="17" height="14" viewBox="0 0 17 14"><path d="M1 7l5 5L16 1" fill="none" stroke="#777" stroke-width="2"/></svg>Learn how to become a trader</li>
  </ul>
  <div class="student" role="img" aria-label="Photo of a smiling student holding a laptop and books"></div>
</section>

<section class="abs card join">
  <div class="band"><span class="arrow"><svg width="12" height="18" viewBox="0 0 12 18"><path d="M2 1l8 8-8 8" fill="none" stroke="#fff" stroke-width="1.8"/></svg></span><h2>JOIN OUR SCHOOL NOW!</h2></div>
  <div class="field" style="top:66px">First name</div>
  <div class="field" style="top:116px">Last name</div>
  <div class="field" style="top:165px">Email</div>
  <div class="agree"><span class="radio"><i></i></span>Agree with our terms and Conditions</div>
  <a class="btn">SUBMIT</a>
</section>

<section class="abs card offers">
  <div class="band"><span class="arrow"><svg width="12" height="18" viewBox="0 0 12 18"><path d="M2 1l8 8-8 8" fill="none" stroke="#fff" stroke-width="1.8"/></svg></span><h2>WHAT DO WE OFFERS?</h2></div>
  <div class="offers-visual" role="img" aria-label="Photo of hands holding a tablet with floating online service icons"></div>
  <p>Lorem ipsum dolor sit amet, consectetur adipisicing elit, sed do eiusmod tempor incididunt ut labore et dolore magna aliqua. Ut enim ad minim veniam, quis nostrud exercitation ullamco laboris nisi ut aliquip ex ea commodo con-sequat. Duis aute irure dolor in reprehenderit in voluptate velit esse cillum dolore eu fugiat .... <b>READ MORE&gt;</b></p>
</section>

<footer class="abs footer">
  <div class="links"><span>Terms and conditions</span>|<span>Privacy Protection</span></div>
  <div class="copy">@Copyright 2016. All right reserved by the Company.</div>
</footer>
</body>
</html>
```